Webdesign für Konfigurator für individuelle Nahrungsergänzungsmittel
Zielgruppe
Die Sternperle (sternperle.de) ist Deutschlands erster Konfigurator für individuelle Nahrungsergänzungsmittel.
Wir stellen jedes Produkt von Hand her und fertigen ausschließlich in unserer Manufaktur in Halvenbrück. Jedes hergestellte Produkt ist individualisiert und trägt den Namen des Käufers.
Unsere Kunden/Kundinnen (ab jetzt ohne Gendern weiter, das wird sonst so sperrig) können sich aus über 180 Rohstoffen bedienen, diese frei kombinieren und von uns in eine Kapsel pressen lassen. Nicht nur die Inhaltsstoffe, auch die Farbe der Kapseln und auch unsere nachhaltige Verpackung (aus Papier und Kork) kann individuell gestaltet werden. Unsere Kunden sind Endkunden, Therapeuten und Händler.
*Wer sind unsere Kunden:
1.) Endkunden mit bekannten Problemen oder dem Wunsch, sich und seinem Körper etwas Gutes zu tun. ('Ich möchte meine Haut und mein Immunsystem unterstützen.')
2.) Endkunden, welche bereits ein oder mehrere Nahrungsergänzungen einnehmen und diese Einnahme vereinfachen wollen ('Nun alles in einer Kapsel')
3.) Endkunden, welche direkte Empfehlungen erhalten haben ('Nimm dies und das.')
4.) Ärzte, Heilpraktiker, Mykotherapeuten, Physiotherapeuten, Ernährungsberater, andere Heilberufe: wir bieten ein spannendes Partnerprogramm, welches dem Therapeuten erlaubt, Nahrungsergänzungen direkt für die Patienten zu konfigurieren. Der Fachmann wählt also die passenden Inhaltsstoffe aus unserem Portfolio aus. Die Dose trägt das Logo, den Namen und die Farbe der jeweiligen Praxis (wird mit dem Kundenkonto verknüpft). Der Patient bekommt eine Vorkasse-Rechnung vom Therapeuten mit und zahlt direkt an die Sternperle, welche das Paket nach Geldeingang direkt an den Patienten versendet. Der Therapeut profitiert durch sein Corporate Design wie auch durch eine Provision.
5.) Händler. Als Manufaktur bieten wir Kleinunternehmern die Möglichkeit, eigene Produkte für den Weiterverkauf herzustellen. Anders als große Loh..
Aufgabenstellung
Logo und CI kann dem bisherigen Design entnommen werden.
Die 'Löffel-Illustration' muss in Grundzügen übernommen werden, kann aber durchaus verändert werden.
Unsere Plattform ist Shopware 6.
Die verwendete Schriftarten sind Bitter und Calibri - dies ist aber nicht verpflichtend.

```html
<!DOCTYPE html>
<html lang="de">
<head>
<meta charset="utf-8">
<title>Sternperle – Individuelle Nahrungsergänzung</title>
<link href="https://fonts.googleapis.com/css2?family=Montserrat:wght@400;500;600;700&family=Open+Sans:wght@400&display=swap" rel="stylesheet">
<style>
:root{
  --ink:#1f2330;
  --text:#6b6f7a;
  --link-blue:#2c5aa0;
  --pill-bg:#e9eef8;
  --accent:#f4506b;
  --orange:#f2a03a;
  --navy:#0d4a7e;
  --partner:#8ba6c2;
  --footer:#222222;
  --footer-link:#2ea3f2;
  --white:#ffffff;
}
*{margin:0;padding:0;box-sizing:border-box}
html,body{width:975px;height:1200px;overflow:hidden;background:var(--white)}
body{position:relative;font-family:'Montserrat',sans-serif;color:var(--ink)}
.abs{position:absolute}
.top-rule{left:17px;top:60px;width:958px;height:2px;background:#f7f8fa}

.audience-card{position:absolute;top:86px;width:166px}
.audience-card .photo{width:166px;height:145px;border-radius:3px}
.audience-card h3{margin-top:16px;font-size:9px;font-weight:600;color:var(--ink)}
.audience-card p{margin-top:6px;font-size:6.4px;line-height:13px;color:var(--text)}
.pill-link{position:absolute;top:247px;left:0;width:76px;height:28px;border-radius:14px;background:var(--pill-bg);color:var(--link-blue);font-size:7px;font-weight:500;display:flex;align-items:center;justify-content:center;box-shadow:0 3px 8px rgba(60,90,160,.12)}

.feature{position:absolute;left:219px;width:263px;height:94px;border-radius:3px;overflow:hidden}
.feature .badge{position:absolute;left:62px;top:11px;width:39px;height:39px;border-radius:50%;display:flex;align-items:center;justify-content:center}
.feature .label{position:absolute;left:0;width:162px;top:65px;text-align:center;font-size:9px;font-weight:500}
.f-blue{top:428px;background:linear-gradient(100deg,#8fb6f2,#b9d2f8 60%,#dce8fb)}
.f-blue .badge{background:#1650b8}.f-blue .label{color:#1e4d9a}
.f-pink{top:537px;background:linear-gradient(100deg,#f7c2cf,#f7cdd7 55%,#e9b6b9)}
.f-pink .badge{background:#f04a67}.f-pink .label{color:#ee4a68}
.f-gold{top:647px;background:linear-gradient(100deg,#fde3b2,#fdeccc 60%,#fbf1df)}
.f-gold .badge{background:#f59b11}.f-gold .label{color:#f0a02c}

.kicker{font-size:8px;letter-spacing:1.4px;font-weight:500;text-transform:uppercase}
.promo{left:512px;top:481px;width:205px}
.promo .kicker{color:var(--orange)}
.promo h2{margin-top:10px;font-size:21px;line-height:29px;font-weight:700;color:var(--ink)}
.promo p{margin-top:9px;font-size:7.8px;line-height:14.7px;color:var(--text)}
.cta{display:flex;align-items:center;justify-content:center;background:var(--accent);color:var(--white);font-weight:700;font-size:7px;border-radius:14px;box-shadow:0 4px 10px rgba(244,80,107,.35)}
.promo .cta{position:absolute;left:0;top:179px;width:78px;height:28px}
.bowl{left:696px;top:387px;width:279px;height:351px;background:radial-gradient(ellipse 60% 55% at 95% 55%,#f2f2f0 0%,#e3e3e1 45%,#c9ccd0 62%,rgba(225,235,250,.5) 75%,rgba(255,255,255,0) 90%)}

.trust{left:17px;top:799px;width:958px;height:257px;background:var(--navy)}
.trust-copy{left:220px;top:810px;width:270px;color:var(--white)}
.trust-copy .kicker{font-weight:600;letter-spacing:1.3px;font-size:8.3px}
.trust-copy h2{margin-top:9px;font-size:20px;line-height:28.5px;font-weight:700}
.trust-copy p{margin-top:8px;font-size:8px;line-height:14.6px;font-weight:500}
.trust-copy .cta{margin-top:12px;width:60px;height:28px}
.partner{position:absolute;transform:translate(-50%,-50%);display:flex;align-items:center;gap:5px;color:var(--partner);font-size:12px;font-weight:600;white-space:nowrap}
.partner i{display:block;width:9px;height:9px;background:var(--partner)}

.site-footer{left:17px;top:1056px;width:958px;height:144px;background:var(--footer);font-family:'Open Sans',sans-serif}
.footer-links{position:absolute;left:203px;top:29px;font-size:9px;line-height:9.5px;color:var(--footer-link)}
.footer-date{position:absolute;left:203px;top:57px;font-size:6.8px;color:var(--white)}
.footer-date::before{content:"";display:inline-block;width:3px;height:3px;border-radius:50%;background:var(--footer-link);margin-right:4px;vertical-align:middle}
.footer-company{position:absolute;left:203px;top:101px;font-size:9px;color:var(--footer-link)}
</style>
</head>
<body>
<div class="abs top-rule"></div>

<article class="audience-card" style="left:219px">
  <div class="photo" role="img" aria-label="Foto: Therapeutin mit Klemmbrett im Gespräch mit einem Patienten" style="background:linear-gradient(120deg,#ece8e6,#c9c7cc 50%,#3f4d66)"></div>
  <h3>Therapeut</h3>
  <p>Eine reiche Auswahl an Inhaltsstoffen für deine Patienten. Produziert wird in Deutschland und schnelle Lieferung ist garantiert…</p>
  <a class="pill-link" style="top:247px">Erfahre mehr</a>
</article>
<article class="audience-card" style="left:414px">
  <div class="photo" role="img" aria-label="Foto: Blutdruckmessung am Arm eines Patienten" style="background:linear-gradient(120deg,#f0ece8,#d9b9a6 45%,#2d3140 75%,#8a6e5d)"></div>
  <h3>Händler</h3>
  <p>Lorem ipsum dolor sit amet, consectetur adipiscing elit, sed do eiusmod tempor incididunt ut labore et dolore magna aliqua de do eusi mlkjkljöljdfk Ei …</p>
  <a class="pill-link">Erfahre mehr</a>
</article>
<article class="audience-card" style="left:610px">
  <div class="photo" role="img" aria-label="Foto: Weiße Tabletten und Kapselgläser auf grauem Stein" style="background:linear-gradient(135deg,#c9cbcf,#dcdde0 55%,#c3c5c9)"></div>
  <h3>Privatkunde</h3>
  <p>Lorem ipsum dolor sit amet, consectetur adipiscing elit, sed do eiusmod tempor incididunt ut labore et dolore magna aliqua. Lorem adipiscing elit, do ei …</p>
  <a class="pill-link">Erfahre mehr</a>
</article>

<div class="feature f-blue" role="img" aria-label="Hintergrund: verstreute weiße Kapseln">
  <div class="badge"><svg width="13" height="13" viewBox="0 0 24 24"><path d="M19 12a7 7 0 1 1-2.1-5" fill="none" stroke="#fff" stroke-width="3.5" stroke-linecap="round"/><path d="M20 3v6h-6z" fill="#fff"/></svg></div>
  <div class="label">50 Anwendungsbereiche</div>
</div>
<div class="feature f-pink" role="img" aria-label="Hintergrund: Foto eines Kindes">
  <div class="badge"><svg width="12" height="12" viewBox="0 0 24 24" fill="#fff"><circle cx="8" cy="7" r="4"/><circle cx="16" cy="8" r="3.5"/><path d="M1 20c0-5 3-8 7-8s7 3 7 8z"/><path d="M13 20c0-4 1-7 4-7s5 3 5 7z"/></svg></div>
  <div class="label">180 Inhaltsstoffe</div>
</div>
<div class="feature f-gold" role="img" aria-label="Hintergrund: Stift auf einem Notizblatt">
  <div class="badge"><svg width="12" height="12" viewBox="0 0 24 24" fill="#fff"><path d="M5 2h10l5 5v15H5z"/><path d="M9 12h7v2H9zm0 4h7v2H9z" fill="#f59b11"/></svg></div>
  <div class="label">Vorteil der Sternperle</div>
</div>

<div class="abs bowl" role="img" aria-label="Foto: Schale voller weißer Tabletten"></div>
<section class="abs promo">
  <div class="kicker">Full Service Pharmacy</div>
  <h2>Sternperle für Dich &amp; Deine Familie.</h2>
  <p>Lorem ipsum dolor sit amet, consectetur adipiscing elit, sed do eiusmod tempor incididunt ut labore et dolore magna aliqua. Ut enim ad minim veniam, quis nostrud.</p>
  <a class="cta">Bestelle Jetzt</a>
</section>

<div class="abs trust"></div>
<section class="abs trust-copy">
  <div class="kicker">Therapeutisch bestätigt</div>
  <h2>Von Therapeuten &amp; Patienten empfohlen.</h2>
  <p>Über 1000 Kunden haben mit der Sternperle … (dies und das erlebt) Lorem ipsum dolor sit amet, consectetur adipiscing elit, sed do eiusmod tempor incididunt ut labore et dolore magna aliqua. Ut enim ad minim veniam, quis nostrud.</p>
  <a class="cta">Über uns</a>
</section>
<div class="partner" style="left:565px;top:835px"><i></i>Nordlicht</div>
<div class="partner" style="left:708px;top:835px">Velmo</div>
<div class="partner" style="left:565px;top:901px">Quarzweg</div>
<div class="partner" style="left:708px;top:901px"><i></i>Tannfeld</div>
<div class="partner" style="left:565px;top:967px">Kornblau</div>
<div class="partner" style="left:708px;top:967px">Wellstrom</div>

<footer class="abs site-footer">
  <div class="footer-links">Impressum Datenschutz<br>AGB</div>
  <div class="footer-date">Juli 2022</div>
  <div class="footer-company">Sternperle GmbH</div>
</footer>
</body>
</html>
```